Desserts Business Card Design

I own a dessert business and cakes and cupcakes are my biggest sellers. I have been running this as a part time business since 2007. I am now looking to expand going full time and open a store front within he next 12 months.
With this expansion I am looking to have my own design setup for the business.

I have been using a design on my cards provided to me by a website I got the cards from. I would like a more original design I can use for the cards, the store front and any other advertising I will be doing. I also have a saying on the back of my business card which I would like to be worked in as well.
"Desserts are nothing, if not from scratch"

Target Market(s)

Younger and older families of all ethnic backgrounds

Industry/Entity Type

Advertising

Contact Information for Business Card

Maribel's Sugared Treats
Tobias Fenwick
4417 Pinecrest Terrace
Oshawa, Ontario
M3P 7J2

Logo Text

Logo styles of interest
Emblem Logo
Pictorial/Combination Logo
Wordmark Logo
Lettermark Logo
Requirements
Must have
• "Desserts are nothing, if not from scratch"
Nice to have
• Maribel's Sugared Treats - This can actually be turned into a logo which is really what I am looking for. Using MST, converted to a logo? I am really looking to see what you can provide me with.
A cake or cupcake added on the front of the card?
Should not have
• I cannot think of anything right now. I an looking forward to see the imaginations from the design groups

```html
<!DOCTYPE html>
<html lang="en">
<head>
<meta charset="utf-8">
<title>Maribel's Sugared Treats – Business Card</title>
<link rel="stylesheet" href="https://fonts.googleapis.com/css2?family=Source+Sans+3:wght@600;700&family=Roboto+Condensed:wght@700&family=Roboto+Slab:wght@800&display=swap">
<style>
  :root {
    --page: #f2f2f2;
    --magenta: #e2156f;
    --magenta-light: #ec4f93;
    --sun: #f7b21a;
    --sun-deep: #f09a12;
    --ink: #222222;
    --white: #ffffff;
  }
  * { box-sizing: border-box; margin: 0; padding: 0; }
  html, body {
    width: 939px; height: 1200px; overflow: hidden;
    background: radial-gradient(ellipse at center, #ffffff 0%, var(--page) 100%);
  }
  .card {
    position: absolute; left: 138px; width: 663px; height: 394px;
    background: linear-gradient(180deg, var(--magenta-light) 0%, var(--magenta) 60%);
    overflow: hidden;
  }
  .card--front { top: 175px; }
  .card--back { top: 630px; }

  .panel {
    position: absolute; left: 29px; top: 167px; width: 605px; height: 196px;
    background: var(--sun);
    border-radius: 20px 0 20px 20px;
  }
  .card--back .panel { top: 166px; }

  .emblem {
    position: absolute; width: 228px; height: 228px; border-radius: 50%;
    border: 4px solid var(--white);
    padding: 8px;
    background: var(--magenta);
  }
  .emblem__art {
    width: 100%; height: 100%; border-radius: 50%;
    background: radial-gradient(circle at 50% 45%, #fbd35a 0%, var(--sun) 55%, var(--sun-deep) 100%);
  }
  .card--front .emblem { left: 46px; top: 55px; }
  .card--back .emblem { left: 51px; top: 111px; }

  .brand {
    position: absolute; right: 22px; top: 70px; text-align: right;
    font-family: "Source Sans 3", sans-serif; font-weight: 700;
    font-size: 40px; line-height: 1.05; color: var(--white);
  }

  .contact {
    position: absolute; right: 48px; top: 250px; text-align: left;
  }
  .contact__name {
    font-family: "Roboto Condensed", sans-serif; font-weight: 700;
    font-size: 32px; color: var(--magenta); letter-spacing: 0.5px;
    text-shadow: -2px -2px 0 var(--white), 2px -2px 0 var(--white), -2px 2px 0 var(--white), 2px 2px 0 var(--white), 0 2px 0 var(--white), 2px 0 0 var(--white), -2px 0 0 var(--white), 0 -2px 0 var(--white);
    margin-bottom: 6px;
  }
  .contact__address {
    font-family: "Source Sans 3", sans-serif; font-weight: 600;
    font-size: 19px; line-height: 1.3; color: var(--ink);
  }
  .phone {
    position: absolute; left: 53px; top: 320px;
    font-family: "Roboto Slab", serif; font-weight: 800;
    font-size: 25px; color: var(--magenta);
    text-shadow: 1px 1px 0 var(--white);
  }

  .motto {
    position: absolute; left: 52px; top: 42px; width: 560px;
    font-family: "Source Sans 3", sans-serif; font-weight: 700;
    font-size: 31px; line-height: 1.15; color: var(--white);
  }
  .motto__line { display: block; }
  .motto__line--second { text-align: right; }

  .website {
    position: absolute; left: 340px; top: 249px; width: 240px; height: 34px;
    border: 2px solid var(--magenta); border-radius: 9px;
    background: var(--sun);
    box-shadow: 2px 2px 0 var(--white) inset;
    font-family: "Source Sans 3", sans-serif; font-weight: 700;
    font-size: 16px; line-height: 30px; text-align: center; color: var(--ink);
  }
</style>
</head>
<body>
  <section class="card card--front">
    <div class="panel"></div>
    <div class="emblem"><div class="emblem__art" role="img" aria-label="Illustration of a cupcake with pink frosting and a cherry on top"></div></div>
    <div class="brand">Maribel's<br>Sugared Treats</div>
    <div class="contact">
      <div class="contact__name">Tobias Fenwick</div>
      <div class="contact__address">4417 Pinecrest Terrace<br>Oshawa, Ontario M3P 7J2</div>
    </div>
    <div class="phone">289-555-0147</div>
  </section>

  <section class="card card--back">
    <div class="panel"></div>
    <p class="motto">
      <span class="motto__line">"Desserts are nothing,</span>
      <span class="motto__line motto__line--second">if not from scratch"</span>
    </p>
    <div class="emblem"><div class="emblem__art" role="img" aria-label="Illustration of a cupcake with pink frosting and a cherry on top"></div></div>
    <div class="website">www.maribelstreats.com</div>
  </section>
</body>
</html>
```